Real estate agent : TJ Property

I have done the attached logo designed by your company .
My business card description as below:
Name : Daniel Ruiz
Mobile: 0491570156
Email : danielr@tjpropertyhq.net.au
Sales & Property Management

```html
<!DOCTYPE html>
<html lang="en">
<head>
<meta charset="utf-8">
<title>TJ Property — Business Card</title>
<link rel="stylesheet" href="https://fonts.googleapis.com/css2?family=Montserrat:wght@700&family=Arimo:wght@400;700&display=swap">
<style>
  :root {
    --backdrop: #e6e6e6;
    --card: #2f2f2f;
    --card-deep: #262626;
    --decor: #3b3a3b;
    --emboss: #3a3a3a;
    --ink: #ffffff;
    --ink-soft: #e4e4e4;
  }
  * { margin: 0; padding: 0; box-sizing: border-box; }
  html, body {
    width: 1200px; height: 801px; overflow: hidden;
    background: var(--backdrop);
  }
  .stage {
    position: relative; width: 1200px; height: 801px;
    display: flex; align-items: center; justify-content: center; gap: 40px;
  }
  .card {
    position: relative; width: 540px; height: 309px;
    background: var(--card); overflow: hidden;
    box-shadow: 0 10px 24px rgba(0,0,0,0.18);
  }
  /* Front */
  .card-front .decor-ring {
    position: absolute; right: -40px; top: -70px;
    width: 330px; height: 330px;
  }
  .card-front .edge-strip {
    position: absolute; left: 0; right: 0; bottom: 0; height: 7px;
    background: var(--ink);
  }
  .card-front .edge-tab {
    position: absolute; left: 0; bottom: 7px; width: 7px; height: 34px;
    background: var(--ink);
  }
  .brand {
    display: flex; align-items: center; gap: 10px;
    font-family: "Montserrat", sans-serif; font-weight: 700;
    color: var(--ink);
  }
  .brand-mark {
    width: 14px; height: 14px; border-radius: 50%; background: var(--ink);
  }
  .card-front .brand {
    position: absolute; left: 44px; top: 70px;
    font-size: 34px; letter-spacing: 1px;
  }
  .contact-block {
    position: absolute; left: 44px; top: 150px;
    font-family: "Arimo", sans-serif; color: var(--ink);
  }
  .agent-name {
    font-weight: 700; font-size: 19px; letter-spacing: 0.5px;
    text-transform: uppercase;
  }
  .agent-role { font-size: 16px; color: var(--ink-soft); margin-top: 3px; }
  .contact-list { list-style: none; margin-top: 20px; }
  .contact-list li {
    display: flex; align-items: center; gap: 10px;
    font-size: 16px; color: var(--ink-soft); margin-top: 4px;
  }
  .contact-list svg { width: 14px; height: 14px; flex: none; }
  /* Back */
  .card-back { background: linear-gradient(160deg, var(--card) 0%, var(--card-deep) 100%); }
  .card-back .brand {
    position: absolute; inset: 0; justify-content: center;
    font-size: 50px; color: var(--emboss); letter-spacing: 2px;
  }
  .card-back .brand-mark { width: 20px; height: 20px; background: var(--emboss); }
</style>
</head>
<body>
  <main class="stage">
    <section class="card card-front" aria-label="Business card front">
      <svg class="decor-ring" viewBox="0 0 330 330" aria-hidden="true">
        <circle cx="165" cy="165" r="140" fill="none" stroke="var(--decor)" stroke-width="34"/>
      </svg>
      <div class="brand"><span class="brand-mark"></span><span class="brand-name">TJ Property</span></div>
      <div class="contact-block">
        <p class="agent-name">Daniel Ruiz</p>
        <p class="agent-role">Sales &amp; Property Management</p>
        <ul class="contact-list">
          <li>
            <svg viewBox="0 0 16 16" aria-hidden="true"><path d="M4 1.5l2.2 2.8-1.3 1.6c.8 1.8 2.4 3.4 4.2 4.2l1.6-1.3 2.8 2.2-1.4 2.5C6.5 13.3 2.7 9.5 1.5 4.1z" fill="var(--ink)"/></svg>
            <span>0491570156</span>
          </li>
          <li>
            <svg viewBox="0 0 16 16" aria-hidden="true"><rect x="1.5" y="3.5" width="13" height="9" fill="none" stroke="var(--ink)" stroke-width="1.3"/><path d="M1.5 3.5L8 9l6.5-5.5" fill="none" stroke="var(--ink)" stroke-width="1.3"/></svg>
            <span>danielr@tjpropertyhq.net.au</span>
          </li>
        </ul>
      </div>
      <div class="edge-tab"></div>
      <div class="edge-strip"></div>
    </section>

    <section class="card card-back" aria-label="Business card back">
      <div class="brand"><span class="brand-mark"></span><span class="brand-name">TJ Property</span></div>
    </section>
  </main>
</body>
</html>
```